Marketing Booklet - Lumo Vastrel
12 Page Marketing Collateral - Ready for your design with images and content
Marketing Booklet - Lumo Vastrel - Financial Services
Creative Brief
Financial Services
This is a sales tool to banks to tell a story about the damage and risk of a disaster to their business and how our company can provide them preparedness and protection. Audience are bank executives and get bored easily. Tell the story with pictures and edgy design.
Front and back covers are largely created by a previous project and will not require much time. We need the full 12 pages created but we have provided the content, images and suggested layouts. We require your creative and talent to make this a unique booklet. It will be a landscape printed, heavy stock, glossy coat, booklet stapled on the small end. Pages need continuity in design because they will be printed touching each other. Finished product needs to be provided in multiple formats including jpeg, ai and a single PDF document that contains each of the 12 finished pages in order. Finished pages need to be 11 1/4 by 8 3/4 to accommodate the 1/8th inch trim.

```html
<!DOCTYPE html>
<html lang="en">
<head>
<meta charset="utf-8">
<title>Lumo Vastrel – Marketing Booklet Spreads</title>
<link href="https://fonts.googleapis.com/css2?family=Open+Sans:wght@400;600;700;800&family=Lora:ital,wght@1,500;1,700&display=swap" rel="stylesheet">
<style>
:root{
  --stage:#2e2b29;
  --label:#e9e4de;
  --paper:#ffffff;
  --paper-soft:#eef3f7;
  --navy:#0d3c63;
  --blue:#1e6fa8;
  --sky:#5aa6d6;
  --green:#6cb33f;
  --ink:#2a3440;
  --grey:#8a96a3;
  --red:#c0392b;
  --amber:#e0a12a;
}
*{box-sizing:border-box;margin:0;padding:0}
html,body{width:1200px;height:1035px;overflow:hidden;background:var(--stage)}
body{position:relative;font-family:"Open Sans",Arial,sans-serif;color:var(--ink)}
.page{position:absolute;width:280px;height:218px;background:var(--paper);overflow:hidden;box-shadow:0 3px 8px rgba(0,0,0,.45)}
.page-label{position:absolute;font-size:9px;font-weight:700;letter-spacing:.5px;color:var(--label)}
.photo{position:absolute;display:block}
.tone-city{background:linear-gradient(160deg,#6d7886,#3b4450 60%,#9a6a3c)}
.tone-storm{background:linear-gradient(170deg,#3c4656,#77828f 50%,#b07a3a)}
.tone-domino{background:linear-gradient(120deg,#d9d4cc,#8c857c 55%,#3b3733)}
.tone-office{background:linear-gradient(160deg,#b9c6d2,#6f8397 60%,#4a5563)}
.tone-sky{background:linear-gradient(180deg,#9cc4e4,#d7e6f2)}
.tone-band{background:linear-gradient(180deg,#ffffff,#dfe9f1 40%,#0d3c63)}
.brand{display:flex;align-items:center;gap:6px;font-weight:800;color:var(--navy);letter-spacing:1px;white-space:nowrap}
.brand-dot{width:12px;height:12px;border-radius:50%;background:var(--blue);flex:none}
h3{font-weight:700;color:var(--navy)}
.body-text{font-size:4.6px;line-height:1.45;color:var(--ink)}
.list{list-style:none;font-size:4.6px;line-height:1.7}
.list li::before{content:"";display:inline-block;width:3px;height:3px;background:var(--green);margin-right:3px;vertical-align:middle}
.serif{font-family:"Lora",Georgia,serif;font-style:italic}
.pie{position:absolute;border-radius:50%}
.contact{position:absolute;font-size:4.8px;line-height:1.5;color:#dbe6f0;white-space:nowrap}
</style>
</head>
<body>

<!-- Row 1 -->
<span class="page-label" style="left:215px;top:18px">PAGE 1</span>
<section class="page cover-front" style="left:215px;top:34px">
  <div class="brand" style="position:absolute;left:58px;top:88px;font-size:17px"><span class="brand-dot" style="width:22px;height:22px"></span>LUMO VASTREL</div>
  <div class="photo tone-band" role="img" aria-label="Decorative flowing band in blue and green along the bottom edge" style="left:0;bottom:0;width:280px;height:46px"></div>
</section>

<span class="page-label" style="left:503px;top:18px">PAGE 2</span>
<section class="page" style="left:498px;top:34px">
  <div class="photo tone-storm" role="img" aria-label="Collage of disaster scenes: flooded streets, fires and damaged buildings" style="inset:0"></div>
</section>

<span class="page-label" style="left:780px;top:18px">PAGE 3</span>
<section class="page" style="left:775px;top:34px;background:var(--paper-soft)">
  <div class="photo tone-city" role="img" aria-label="Damaged bank building" style="left:22px;top:12px;width:54px;height:38px"></div>
  <div class="photo tone-office" role="img" aria-label="Empty office" style="left:84px;top:12px;width:54px;height:38px"></div>
  <div class="photo tone-storm" role="img" aria-label="Storm over city" style="left:146px;top:12px;width:54px;height:38px"></div>
  <div class="photo tone-sky" role="img" aria-label="Hurricane from above" style="left:208px;top:12px;width:54px;height:38px"></div>
  <p class="serif" style="position:absolute;left:14px;top:60px;width:252px;text-align:center;font-size:11px;color:var(--navy);line-height:1.3">What would it take to separate you from<br>your files… your fans… your Customers!</p>
  <div class="photo tone-storm" role="img" aria-label="Wide view of disaster aftermath" style="left:14px;top:102px;width:252px;height:66px"></div>
  <p class="serif" style="position:absolute;left:14px;top:176px;width:252px;text-align:center;font-size:10px;color:var(--navy);line-height:1.35">There's a new word in Disaster Recovery<br>It's… <b style="color:var(--red)">REALITY!</b></p>
</section>

<!-- Row 2 -->
<span class="page-label" style="left:50px;top:256px">PAGE 4</span>
<section class="page" style="left:45px;top:272px">
  <div class="pie" style="left:20px;top:16px;width:92px;height:92px;background:conic-gradient(#1e6fa8 0 38%,#6cb33f 0 58%,#e0a12a 0 74%,#c0392b 0 86%,#5aa6d6 0)"></div>
  <div class="pie" style="left:150px;top:20px;width:84px;height:84px;background:conic-gradient(#c0392b 0 30%,#1e6fa8 0 55%,#e0a12a 0 72%,#6cb33f 0)"></div>
  <div style="position:absolute;left:14px;top:122px;width:252px;height:84px;background:var(--navy);padding:8px">
    <h3 style="color:#fff;font-size:9px">Did you know?</h3>
    <p class="body-text" style="color:#dbe6f0;font-size:6px;margin-top:4px">Most firms hit by a major outage never reopen within a year.</p>
  </div>
</section>

<span class="page-label" style="left:330px;top:256px">PAGE 5</span>
<section class="page" style="left:325px;top:272px">
  <div class="pie" style="left:14px;top:14px;width:80px;height:80px;background:conic-gradient(#6cb33f 0 45%,#1e6fa8 0 70%,#e0a12a 0 85%,#c0392b 0)"></div>
  <div class="pie" style="left:18px;top:118px;width:74px;height:74px;background:radial-gradient(circle,#fff 0 45%,transparent 46%),conic-gradient(#1e6fa8 0 40%,#c0392b 0 62%,#6cb33f 0 80%,#5aa6d6 0)"></div>
  <div style="position:absolute;left:108px;top:14px;width:160px;height:62px;border:1px solid var(--blue);padding:5px">
    <h3 style="font-size:7px">Business Continuity</h3>
    <p class="body-text" style="color:var(--red);font-weight:700">Critical to our operations</p>
  </div>
  <p style="position:absolute;left:108px;top:88px;width:160px;font-size:6.5px;line-height:1.5;color:var(--navy);text-align:center">Over the last 20 years natural disasters caused losses beyond <b style="font-size:10px;color:var(--red)">2 trillion dollars</b></p>
</section>

<span class="page-label" style="left:610px;top:256px">PAGE 6</span>
<section class="page" style="left:605px;top:272px">
  <div class="photo tone-domino" role="img" aria-label="Row of falling dominoes" style="inset:0"></div>
</section>

<span class="page-label" style="left:890px;top:256px">PAGE 7</span>
<section class="page" style="left:885px;top:272px">
  <div class="photo tone-domino" role="img" aria-label="Close-up of dominoes in a line" style="inset:0"></div>
  <p class="serif" style="position:absolute;right:12px;top:14px;width:150px;text-align:right;font-size:12px;line-height:1.2;color:#fff">When<br>Fiduciary Failure<br>is <b style="color:var(--amber)">NOT</b> an Option</p>
  <p class="body-text" style="position:absolute;left:12px;bottom:12px;width:150px;color:#fff">Regulators expect every bank to protect records, systems and client trust when disaster strikes.</p>
</section>

<!-- Row 3 -->
<span class="page-label" style="left:50px;top:516px">PAGE 8</span>
<section class="page" style="left:45px;top:532px">
  <div class="photo tone-office" role="img" aria-label="Modern bank building exterior" style="left:0;top:0;width:280px;height:92px"></div>
  <div class="brand" style="position:absolute;left:14px;top:102px;font-size:8px"><span class="brand-dot" style="width:9px;height:9px"></span>LUMO VASTREL</div>
  <h3 style="position:absolute;left:14px;top:122px;font-size:11px">The <span style="color:var(--green)">CORE</span> Solution</h3>
  <p class="body-text" style="position:absolute;left:14px;top:142px;width:180px">We bring planning, recovery sites and expert staff together so your bank keeps serving clients through any event.</p>
  <div style="position:absolute;left:0;bottom:0;width:280px;height:8px;background:var(--green)"></div>
</section>

<span class="page-label" style="left:330px;top:516px">PAGE 9</span>
<section class="page" style="left:325px;top:532px">
  <div style="position:absolute;left:0;top:0;width:280px;height:6px;background:var(--navy)"></div>
  <h3 style="position:absolute;left:14px;top:16px;font-size:10px">Our House</h3>
  <p class="body-text" style="position:absolute;left:14px;top:34px;width:130px">Our secure centers stay powered, staffed and connected around the clock.</p>
  <h3 style="position:absolute;left:14px;top:66px;font-size:7px">Continuity Center</h3>
  <p class="body-text" style="position:absolute;left:14px;top:78px;width:130px">Dedicated work areas ready for your team within hours.</p>
  <div class="photo tone-office" role="img" aria-label="Recovery center workroom" style="left:14px;top:110px;width:130px;height:92px"></div>
  <div style="position:absolute;left:156px;top:16px;width:110px;height:186px;background:var(--paper-soft);padding:8px">
    <h3 style="font-size:7px">Supply Resources</h3>
    <ul class="list" style="margin-top:5px"><li>Backup power</li><li>Secure servers</li><li>Staff seating</li><li>Data links</li><li>Phone lines</li><li>Mail handling</li></ul>
  </div>
</section>

<span class="page-label" style="left:610px;top:516px">PAGE 10</span>
<section class="page" style="left:605px;top:532px">
  <div class="photo tone-city" role="img" aria-label="Bank branch street view" style="left:0;top:0;width:280px;height:80px"></div>
  <h3 style="position:absolute;left:14px;top:90px;font-size:10px">Your House</h3>
  <p class="body-text" style="position:absolute;left:14px;top:108px;width:120px">We assess your site, train your people and test your plan each year.</p>
  <h3 style="position:absolute;left:148px;top:92px;font-size:7px">Business Office</h3>
  <ul class="list" style="position:absolute;left:148px;top:104px"><li>Risk review</li><li>Plan design</li></ul>
  <h3 style="position:absolute;left:148px;top:134px;font-size:7px">Branch Network</h3>
  <ul class="list" style="position:absolute;left:148px;top:146px"><li>Staff drills</li><li>Annual testing</li></ul>
  <div style="position:absolute;left:0;bottom:0;width:280px;height:8px;background:var(--green)"></div>
</section>

<span class="page-label" style="left:892px;top:516px">PAGE 11</span>
<section class="page" style="left:887px;top:532px">
  <div style="position:absolute;left:0;top:0;width:280px;height:40px;background:var(--paper-soft);padding:8px 14px">
    <h3 style="font-size:12px">The Core Package</h3>
    <p class="body-text" style="color:var(--blue)">Everything your bank needs in one plan</p>
  </div>
  <h3 style="position:absolute;left:14px;top:50px;font-size:8px">Our House</h3>
  <ul class="list" style="position:absolute;left:14px;top:64px"><li>Recovery seats</li><li>Data vaulting</li><li>Power backup</li><li>On-site support</li></ul>
  <h3 style="position:absolute;left:148px;top:50px;font-size:8px">Your House</h3>
  <ul class="list" style="position:absolute;left:148px;top:64px"><li>Risk audit</li><li>Plan writing</li><li>Team training</li><li>Yearly tests</li></ul>
  <div class="photo tone-office" role="img" aria-label="Bank staff at work" style="left:14px;top:130px;width:120px;height:74px"></div>
  <div class="photo tone-city" role="img" aria-label="Recovery site building" style="left:146px;top:130px;width:120px;height:74px"></div>
</section>

<!-- Row 4 -->
<span class="page-label" style="left:402px;top:987px">PAGE 12</span>
<section class="page cover-back" style="left:397px;top:765px;background:radial-gradient(circle at 30% 20%,#1e6fa8,#0d3c63 55%,#071f36)">
  <div class="brand" style="position:absolute;left:30px;top:152px;font-size:7px;color:#fff"><span class="brand-dot" style="width:8px;height:8px;background:var(--green)"></span>LUMO VASTREL</div>
  <div class="contact" style="left:136px;top:140px">
    Lumo Vastrel<br>1200 Harbor Point Drive<br>Suite 400, Marlow, TX 75001<br>Phone 555 014 2290<br>info@lumovastrel.com
  </div>
</section>

</body>
</html>
```